Fashion-Doll Website

I'm looking to create a new and better website for my growing fashion-doll brand, MARZELL.

About me: I'm a Brooklyn-based artist, illustrator, and doll-maker and MARZELL is the name of my doll. Marzell is a character doll (one girl) but she's not necessarily defined by any particular physical trait outside of the sculpt of the doll and her unique sense of style. For example, she could have pink hair and freckles or dark skin and green eyes, but she would still be "Marzell."

My partner and I created the current website ourselves using Adobe Muse. While it has served its purpose, we are not professional graphic or web designers, so I'm looking to graduate to a much more sophisticated and streamlined web design. I want the site to feel sweet and homespun but also hip and edgy. Because the site is so image heavy, I think black and white or black and off-white might be the best color palate, but I'm open to seeing other palates. Marzell's signature color is a muted lavender so maybe that could be integrated into the design. Here is the link:

www.MarzellFigure.example

I want the website to feel more like a shop and less like a gallery/info page. I'm now selling one-of-a-kind porcelain dolls, limited-edition resin dolls, face-plate necklaces, paper dolls, custom doll services, and printed Marzell throw pillows. I also need an interface that will allow me to create new categories, update inventory, and post new items easily.

I need to add new sections for press/articles, multiple image galleries (photography, products, illustrations, comics, and fan art), **collaboration projects, and several flash based doll "dress-up" games.

I would prefer a design that I can code/update myself using Adobe Muse. PSD files import into Muse, so I would prefer that you use them. I'm certainly not opposed to other designs, but I would prefer a design I can manage myself.

I'm including some photos and drawings of Marzell that express her look and vibe. I don't want to use these images in the web design necessarily (I think simple is best) but I thought they would be helpful in expressing the kind of girl she is and how I want the site to feel. I want to work with someone who has a clean, refined, yet whimsical aesthetic who can help me create a website that really expresses how special Marzell is.

Reason: I have had a family emergency come up and I can't devote time to this right now so I'm extending the deadline another 10 days.

Target Market(s)

young eccentrics, art collectors, fashion enthusiasts, and adult doll-collectors

Industry/Entity Type

Fashion

Requirements
Must have
• I need the following main categories: Info, Sales, Galleries, Press, and Dress-up. However, I don't necessarily want or expect the layout to be organized like the current website.

INFO:

*About Marzell (the character)

*Doll specifications: 27" porcelain doll, 22" porcelain doll, 22" resin doll, life-size doll (for window display)

*About the artist

SALES:

*Porcelain dolls

*Resin dolls

*Face-plate necklaces

*Pillows

*Custom doll/necklace info and inquiry form

GALLERIES:

*Photographs

*Collaboration projects

*Illustrations/Comics

*Fan Art/Contests

PRESS:

*An inventory of pdf's of articles about Marzell for users to download or view inside a reader online.

DRESS UP:

*Links to two interactive flash based dress-up games (interactive paper dolls)

Nice to have
• I hold online drawing and design contests from time to time so I would love to have a spot on the site reserved to host the rules and results of my contests.

Marzell has a large facebook and Instagram following so links to her social media would also be great.
instagram: @marzellfigure
facebook: facebook.com/marzellfigure

Should not have
• I'm not looking to see anything too girly, too young, or too sexy.
Marzell is not Tovanna, Velmont Kid, or Quirvs. She's a sophisticated young girl who is fresh, funky, and free-spirited.

```html
<!DOCTYPE html>
<html lang="en">
<head>
<meta charset="utf-8">
<title>Marzell Dolls</title>
<link href="https://fonts.googleapis.com/css2?family=Source+Sans+3:wght@300;400;600&family=Poiret+One&display=swap" rel="stylesheet">
<style>
:root{
  --page:#f1efed;
  --ink:#2a2624;
  --body:#3f3a37;
  --muted:#6d6762;
  --accent:#e0651e;
  --accent-light:#f7953a;
  --hero-dark:#1e1416;
  --hero-mid:#3a2a2c;
  --menu:#5f5859;
  --menu-line:#4a4344;
  --frame:#dcd9d6;
  --panel:#ffffff;
  --border:#e1dedb;
  --sub:#a79a9a;
}
*{box-sizing:border-box;margin:0;padding:0}
html,body{width:1195px;height:1200px;overflow:hidden}
body{background:var(--page);font-family:"Source Sans 3",Arial,sans-serif;color:var(--body);position:relative}
.abs{position:absolute}
.logo{left:100px;top:40px;font-family:"Poiret One",sans-serif;font-size:66px;letter-spacing:4px;color:var(--ink);line-height:1}
.social{display:flex;gap:12px}
.social span{width:37px;height:37px;background:#3b3838;border-radius:4px;display:block}
.social.top{left:1009px;top:36px}
.social.bottom{left:1011px;top:1128px}
.main-nav{right:98px;top:103px;display:flex;gap:32px;font-size:16px;color:var(--muted)}
.main-nav .current{color:var(--ink);font-weight:600}
.hero{left:99px;top:154px;width:998px;height:322px;background:var(--frame);padding:8px}
.hero-inner{position:relative;width:100%;height:100%;background:linear-gradient(90deg,var(--hero-dark),var(--hero-mid) 55%,var(--hero-dark));overflow:hidden}
.hero-photo{position:absolute;left:0;top:0;width:281px;height:100%;background:linear-gradient(135deg,#3a2a2e,#c9a7b3 45%,#e8d4da 70%,#6b5258)}
.hero-title{position:absolute;left:311px;top:36px;width:360px;font-weight:300;font-size:35px;line-height:41px;color:#f3eeee}
.hero-sub{position:absolute;left:311px;top:160px;font-weight:300;font-size:24px;color:var(--sub)}
.dots{position:absolute;left:455px;top:270px;display:flex;gap:9px}
.dots i{width:14px;height:14px;border-radius:50%;background:#8a8283;display:block}
.dots i.on{background:#fff}
.cat-menu{position:absolute;left:715px;top:24px;width:243px;background:var(--menu);border-radius:3px;list-style:none}
.cat-menu li{height:48px;display:flex;align-items:center;padding-left:26px;font-size:20px;font-weight:600;color:#fff;border-bottom:1px solid var(--menu-line)}
.cat-menu li:last-child{border-bottom:none;height:52px}
.cat-menu svg{margin-right:18px}
.content{left:99px;top:490px;width:998px;height:605px;background:var(--panel);border:1px solid var(--border)}
h2.section{font-weight:300;color:var(--accent);font-size:29px}
.welcome-title{left:122px;top:512px}
.intro{left:122px;top:560px;width:660px;font-size:14px;line-height:25px}
.doll-art{left:126px;top:645px;width:220px;height:230px;background:radial-gradient(ellipse at center,#d4a090 0%,#e8d8d0 45%,#ffffff 75%)}
.lorem{left:386px;top:648px;width:394px;font-size:14px;line-height:25px;text-align:justify}
.divider{left:118px;top:890px;width:662px;height:1px;background:var(--border)}
.view-all{right:415px;top:910px;font-size:12.5px;color:var(--ink);text-transform:uppercase}
.thumb{top:938px;width:206px;height:127px;border:3px solid #d6d3d1}
.t1{left:120px;background:linear-gradient(135deg,#c9b9d6,#e6d79a 50%,#b7b9c4)}
.t2{left:346px;background:radial-gradient(circle at 50% 45%,#f0dccf,#d8c9bf 55%,#b64a4a 80%)}
.t3{left:573px;background:radial-gradient(circle at 50% 45%,#f2ce90,#e58bb8 55%,#2a2325 90%)}
.contest{left:822px;top:518px;width:251px;height:344px;border:1px solid var(--border);background:#f8f7f6;padding:24px 22px}
.contest h3{color:var(--accent);font-weight:400;font-size:25px;line-height:29px;text-align:center;text-transform:uppercase}
.contest p{margin-top:20px;font-size:14px;line-height:23px;text-align:justify;color:var(--muted)}
.btn-participate{left:880px;top:783px;width:172px;height:46px;background:linear-gradient(var(--accent-light),var(--accent));border-radius:3px;color:#fff;font-weight:600;font-size:16px;display:flex;align-items:center;justify-content:center;padding-left:14px}
.pencil-cup{left:840px;top:772px;width:48px;height:58px;background:linear-gradient(#c7a7d8,#9a9aa0);border-radius:4px 4px 10px 10px}
.news-title{left:822px;top:895px;font-size:27px}
.news-box{left:821px;top:940px;width:253px;height:126px;background:linear-gradient(#2b2828,#4a4646);border-radius:3px}
.email{position:absolute;left:12px;top:19px;width:229px;height:37px;background:#fff;border-radius:2px;font-size:14px;color:#888;padding:10px 19px}
.submit{position:absolute;right:12px;top:72px;width:80px;height:34px;background:linear-gradient(#aaa6a6,#858181);border-radius:2px;color:#fff;font-weight:600;font-size:16px;text-align:center;line-height:34px}
.foot-nav{left:99px;top:1120px;font-size:14px;color:var(--body)}
.foot-nav span{margin:0 9px;color:#999}
.copyright{left:99px;top:1153px;font-size:13px;color:var(--body)}
</style>
</head>
<body>
<div class="abs logo">MARZELL</div>
<div class="abs social top"><span role="img" aria-label="Social profile link"></span><span role="img" aria-label="Photo feed link"></span></div>
<nav class="abs main-nav"><span class="current">Home</span><span>Info</span><span>Sales</span><span>Galleries</span><span>Press</span><span>Dress Up</span></nav>

<section class="abs hero">
  <div class="hero-inner">
    <div class="hero-photo" role="img" aria-label="Photo of a porcelain doll with long pink hair"></div>
    <p class="hero-title">Marzell is a modern take on the classic European fashion doll.</p>
    <p class="hero-sub">Handmade in Bushwick, Brooklyn</p>
    <div class="dots"><i class="on"></i><i></i><i></i><i></i></div>
    <ul class="cat-menu">
      <li><svg width="16" height="14" viewBox="0 0 16 14"><path d="M1 7h12M8 2l5 5-5 5" stroke="#fff" stroke-width="2.5" fill="none"/></svg>Dolls</li>
      <li><svg width="16" height="14" viewBox="0 0 16 14"><path d="M1 7h12M8 2l5 5-5 5" stroke="#fff" stroke-width="2.5" fill="none"/></svg>Necklaces</li>
      <li><svg width="16" height="14" viewBox="0 0 16 14"><path d="M1 7h12M8 2l5 5-5 5" stroke="#fff" stroke-width="2.5" fill="none"/></svg>Pillows</li>
      <li><svg width="16" height="14" viewBox="0 0 16 14"><path d="M1 7h12M8 2l5 5-5 5" stroke="#fff" stroke-width="2.5" fill="none"/></svg>Paper Dolls</li>
      <li><svg width="16" height="14" viewBox="0 0 16 14"><path d="M1 7h12M8 2l5 5-5 5" stroke="#fff" stroke-width="2.5" fill="none"/></svg>Accessories</li>
    </ul>
  </div>
</section>

<div class="abs content"></div>
<h2 class="abs section welcome-title">Welcome to Marzell Dolls</h2>
<p class="abs intro">Each element of Marzell is designed and handcrafted, from the heirloom-quality porcelain to the custom wigs and garments.&nbsp; Her look embodies Brooklyn street-style, Manhattan sophistication, and the classic lines of yesterday.&nbsp; Marzell represents a new chapter in the venerable tradition of boutique doll-making.</p>
<div class="abs doll-art" role="img" aria-label="Illustration of three dolls in colourful dresses"></div>
<p class="abs lorem">Donec sagittis nisi non ante faucibus tempus. Vestibulum id purus id dui venenatis vulputate in eu neque. Quisque quis mauris sit amet dui interdum lobortis. Aenean non leo ac turpis sodales sodales sed id velit. Cras molestie ultrices lectus, vitae luctus nisl. Etiam rutrum dui eu orci elementum, sed porttitor urna consequat. Fusce tristique a lorem vitae congue. Nam eu purus vitae augue lobortis fringilla rutrum a purus. Praesent vitae nibh nec ante consectetur dignissim. Aliquam eleifend facilisis commodo. Sed interdum quam ut erat scelerisque.</p>
<div class="abs divider"></div>
<div class="abs view-all">View all products &raquo;</div>
<div class="abs thumb t1" role="img" aria-label="Illustration of a reclining doll with cushions"></div>
<div class="abs thumb t2" role="img" aria-label="Illustration of a doll with red roses in her hair"></div>
<div class="abs thumb t3" role="img" aria-label="Photo of a model with a flower crown on pink"></div>

<aside class="abs contest">
  <h3>Drawing/ Design Contests</h3>
  <p>Nam nisl velit, lobortis ac dolor non, suscipit blandit diam. Phasellus port titor felis eu turpis consectetur accumsan. Fusce blandit semper leo, quis fringilla eros eleifend eget.</p>
</aside>
<div class="abs btn-participate">PARTICIPATE NOW</div>
<div class="abs pencil-cup" role="img" aria-label="Cup of coloured pencils"></div>

<h2 class="abs section news-title">Newsletter Sign Up</h2>
<div class="abs news-box">
  <div class="email">Email</div>
  <div class="submit">SUBMIT</div>
</div>

<nav class="abs foot-nav">Home<span>|</span>Info<span>|</span>Sales<span>|</span>Galleries<span>|</span>Press<span>|</span>Dress Up</nav>
<p class="abs copyright">Copyright &copy; 2013 Marzellfigure.&nbsp;&nbsp; All rights reserved.</p>
<div class="abs social bottom"><span role="img" aria-label="Social profile link"></span><span role="img" aria-label="Photo feed link"></span></div>
</body>
</html>
```